【 概要 】 IT系資格試験の過去問題を学習できるサイトで、 有料の会員(メンバー)に向けて、広告の非表示や、解説データの提供、追加機能などのサービスを提供しております。 サービスのトップページに掲載するバナー画像を募集します。 リンク先となるメンバーシップ紹介ページ https://www.sorairogakushu.com/membership/ 【 依頼内容 】 ・サイズ: 横1,280px × 縦200px(表示サイズはPC:横500px、縦80px、SP:横全幅) ・作成数: 1種類 ・利用用途:ウェブサイト ・掲載場所(現在は違うバナー画像が掲載されています) 【PC表示】https://www.sorairogakushu.com/hkrenshu.php 【SP 表示 】 https://www.sorairogakushu.com/s/hkrenshu.php 【 デザインイメージ 】 ・ターゲット層:20〜40代男性 ・雰囲気:サイトのイメージに合うスマートな印象、ごちゃごちゃしていない、"売り売り"していない ・上記掲載場所のサイトは水色メインの配色ですが、別の同じようなサイトでも使いたいのでどの配色にでも合うものだと嬉しいです。 ・金額の記載はなし 【 契約金額(税抜) 】 4,000円 ※契約金額(税込)からシステム利用料を差し引いた金額が、ワーカーさまの受取金額となります 。 ※本依頼に申込みをいただいた段階で、作成していただいたバナー画像の著作権は当方に譲渡するものとし、 作成していただくバナー画像について著作権人格権を行使しないことについて同意を得たとみなします。 その他ご質問等ありましたら、気軽にお問い合わせください。 いただいた提案が多い場合には、個別に返信できかねる場合がございますのでご了承くださいませ。 ご応募をお待ちしております! |
実際のサイト上に合わせてみたところマッチしていて、私の好みのイメージでもありました。また、利用者の合格をイメージさせるデザインが大変よく採用に至りました。サイト名が入っていないので他のサイトへの表示が編集なく行えることもポイントでした。
皆さま、この度はお時間を使ってご提案くださり誠にありがとうございました。いただいたメッセージに個々に返信することができず申し訳ございません。
本当に素晴らしいデザインが多く、また非常にたくさんのご提案をいただいたので決めるのが大変という嬉しい悲鳴でした。
今後もバナー等デザインのお仕事をするときにはこちらに依頼させていただこうと思います。

```html
<!DOCTYPE html>
<html lang="ja">
<head>
<meta charset="UTF-8">
<title>メンバーシップ制度バナー</title>
<link href="https://fonts.googleapis.com/css2?family=Noto+Sans+JP:wght@700;900&display=swap" rel="stylesheet">
<style>
  :root {
    --paper: #f3f4f6;
    --grid-line: #dde2e8;
    --ink: #1f2b3d;
    --label-bg: #ffffff;
    --accent: #f8c04a;
    --accent-deep: #f3a23a;
    --sky: #8ec9ef;
    --sky-soft: #d7ecfa;
    --white: #ffffff;
  }
  html, body {
    margin: 0;
    padding: 0;
    overflow: hidden;
  }
  body {
    width: 1200px;
    height: 188px;
    font-family: "Noto Sans JP", sans-serif;
  }
  .banner {
    position: relative;
    width: 1200px;
    height: 188px;
    overflow: hidden;
    background-color: var(--paper);
    background-image:
      linear-gradient(var(--grid-line) 1px, transparent 1px),
      linear-gradient(90deg, var(--grid-line) 1px, transparent 1px);
    background-size: 22px 22px;
  }
  .goal-scene {
    position: absolute;
    left: 730px;
    top: 0;
    width: 380px;
    height: 188px;
    z-index: 1;
    background: linear-gradient(120deg, rgba(243,244,246,0) 0%, var(--sky-soft) 30%, var(--sky) 60%, rgba(243,244,246,0) 100%);
  }
  .lead {
    position: absolute;
    z-index: 2;
    left: 44px;
    top: 26px;
    margin: 0;
    padding: 3px 14px;
    background: var(--label-bg);
    color: var(--ink);
    font-size: 30px;
    font-weight: 900;
    letter-spacing: 0.04em;
    line-height: 1.25;
    white-space: nowrap;
  }
  .title {
    position: absolute;
    z-index: 2;
    left: 44px;
    top: 88px;
    margin: 0;
    padding: 0 16px 4px;
    background: linear-gradient(180deg, var(--accent) 0%, var(--accent-deep) 100%);
    color: var(--white);
    font-size: 64px;
    font-weight: 900;
    letter-spacing: 0.1em;
    line-height: 1.15;
    white-space: nowrap;
  }
  .perk-corner {
    position: absolute;
    z-index: 2;
    right: 0;
    bottom: 0;
    width: 110px;
    height: 110px;
  }
  .perk-corner svg {
    position: absolute;
    inset: 0;
  }
  .perk-label {
    position: absolute;
    right: -2px;
    bottom: 24px;
    width: 100px;
    text-align: center;
    transform: rotate(-45deg);
    color: var(--white);
    font-weight: 900;
    font-size: 16px;
    line-height: 1.05;
    letter-spacing: 0.04em;
  }
</style>
</head>
<body>
  <div class="banner">
    <div class="goal-scene" role="img" aria-label="上昇する水色の矢印とゴールテープを切って喜ぶビジネスマンたちのイラスト"></div>
    <p class="lead">より速く、より快適に試験合格を目指すなら</p>
    <h1 class="title">メンバーシップ制度</h1>
    <div class="perk-corner">
      <svg width="110" height="110" viewBox="0 0 110 110" aria-hidden="true">
        <path d="M110,0 L110,110 L0,110 Q70,80 110,0 Z" fill="var(--accent-deep)"/>
      </svg>
      <div class="perk-label">特典<br>CHECK</div>
    </div>
  </div>
</body>
</html>
```